exquisite label design for foam cleanser

Kindly invite you to design bottle label (102 mm*64 mm) for our product, a kind of foam cleanser for wearable aligners. The color of bottle and liquid inside are both clear, but the foam pump is white. You could download the pic of bottle among the uploaded files. I have no KV of our website or posters to supply you, except the logo file attached. Content on the label is attached too. Please check it. I wish the label would make our product look high-end and reliable. And it would be better if you could give some advice on paper material and special requirements for printing, related to your design. I value the texture of label too, because I think that stands for the quality of products. No color limitation for the use of our logo, and please ignore the Chinese characters in our logo, they are not in our plan.
Target Market(s)
16-35 female, orthodontic patients.
Colors
Designer to choose colors to be used in the design.
Look and feel

```html
<!DOCTYPE html>
<html lang="en">
<head>
<meta charset="UTF-8">
<title>Clarevo Aligner Cleansing Foam – Label</title>
<link rel="stylesheet" href="https://fonts.googleapis.com/css2?family=Poppins:wght@500;600;700&family=Noto+Sans+TC:wght@400&display=swap">
<style>
  :root {
    --page-bg: #f2f2f3;
    --label-bg-top: #ffffff;
    --label-bg-bottom: #eeeeef;
    --brand-blue: #2fa6dc;
    --brand-blue-light: #6cc1ea;
    --ink: #1d1d1f;
    --white: #ffffff;
  }
  * { margin: 0; padding: 0; box-sizing: border-box; }
  html, body {
    width: 1200px;
    height: 1200px;
    overflow: hidden;
    background: var(--page-bg);
  }
  .canvas {
    position: relative;
    width: 1200px;
    height: 1200px;
  }
  .label {
    position: absolute;
    left: 379px;
    top: 95px;
    width: 442px;
    height: 1011px;
    background: linear-gradient(90deg, var(--label-bg-bottom) 0%, var(--label-bg-top) 30%, var(--label-bg-top) 60%, var(--label-bg-bottom) 100%);
    font-family: "Poppins", sans-serif;
    color: var(--ink);
    text-align: center;
  }
  .edge-band {
    position: absolute;
    left: 0;
    width: 100%;
    height: 27px;
    background: var(--brand-blue);
  }
  .edge-band--top { top: 0; }
  .edge-band--bottom { bottom: 0; }
  .brand-name {
    position: absolute;
    left: 0;
    width: 100%;
    top: 160px;
    font-size: 74px;
    font-weight: 700;
    line-height: 1;
    color: var(--brand-blue);
    letter-spacing: 1px;
  }
  .product-type {
    position: absolute;
    left: 0;
    width: 100%;
    top: 362px;
    font-family: "Noto Sans TC", sans-serif;
    font-size: 38px;
    font-weight: 400;
    line-height: 1.2;
    letter-spacing: 1px;
  }
  .benefits {
    position: absolute;
    left: 0;
    width: 100%;
    top: 482px;
    font-size: 45px;
    font-weight: 600;
    line-height: 56px;
  }
  .flavor-band {
    position: absolute;
    left: 0;
    top: 741px;
    width: 100%;
    height: 59px;
    background: linear-gradient(90deg, var(--brand-blue) 0%, var(--brand-blue) 55%, var(--brand-blue-light) 100%);
    color: var(--white);
    font-size: 48px;
    font-weight: 600;
    line-height: 59px;
  }
  .volume {
    position: absolute;
    left: 0;
    width: 100%;
    top: 870px;
    font-size: 21px;
    font-weight: 500;
    line-height: 1.2;
  }
</style>
</head>
<body>
  <main class="canvas">
    <section class="label">
      <div class="edge-band edge-band--top"></div>

      <h1 class="brand-name">Clarevo</h1>

      <p class="product-type">隱形牙套清潔泡沫</p>

      <p class="benefits">Deep Cleaning<br>&amp;<br>Lasting Freshness</p>

      <div class="flavor-band">Mint Flavor</div>

      <p class="volume">1.69 Fl Oz / 50ml</p>

      <div class="edge-band edge-band--bottom"></div>
    </section>
  </main>
</body>
</html>
```